Steadfast Property Reviews

We need stationery for our new home inspection company. We inspect homes for people prior to purchasing to ensure the property is in good condition, as well as inspecting new homes to ensure they have been built to the appropriate standards. We are happy to look at combinations of colours. The use of a water mark would be good. Open to suggestions.

Industry/Entity Type

Home Inspection

```html
<!DOCTYPE html>
<html lang="en">
<head>
<meta charset="utf-8">
<title>Steadfast Property Reviews — Business Cards</title>
<link rel="stylesheet" href="https://fonts.googleapis.com/css2?family=Questrial&family=Mulish:wght@700&display=swap">
<style>
  :root {
    --brand-blue: #0f4a7c;
    --brand-blue-dark: #0b3d68;
    --wave-grey: #4a4b4f;
    --paper: #f4f5f6;
    --card-white: #ffffff;
    --text-grey: #55575b;
    --backdrop: #e9ebec;
  }
  * { box-sizing: border-box; margin: 0; padding: 0; }
  html, body {
    width: 1200px;
    height: 954px;
    overflow: hidden;
    background: var(--backdrop);
    font-family: "Questrial", sans-serif;
  }
  .sheet {
    width: 1200px;
    height: 954px;
    display: flex;
    align-items: center;
    justify-content: center;
    gap: 48px;
  }
  .card {
    position: relative;
    width: 520px;
    height: 318px;
    overflow: hidden;
    box-shadow: 0 2px 10px rgba(0, 0, 0, 0.12);
  }

  /* Front face */
  .card--front { background: var(--card-white); }
  .card__waves { position: absolute; inset: 0; }
  .wordmark {
    position: absolute;
    display: flex;
    align-items: center;
    gap: 12px;
  }
  .card--front .wordmark { left: 56px; top: 34px; }
  .wordmark__mark {
    width: 34px;
    height: 34px;
    background: var(--brand-blue);
    flex: none;
  }
  .wordmark__name {
    font-family: "Questrial", sans-serif;
    font-size: 22px;
    line-height: 1.05;
    color: var(--brand-blue);
  }
  .holder {
    position: absolute;
    right: 30px;
    top: 112px;
    text-align: right;
  }
  .holder__name {
    font-family: "Mulish", sans-serif;
    font-weight: 700;
    font-size: 13px;
    color: var(--brand-blue);
  }
  .holder__role {
    font-size: 12px;
    color: var(--text-grey);
    margin-top: 2px;
  }
  .contacts {
    position: absolute;
    right: 22px;
    bottom: 14px;
    list-style: none;
    text-align: right;
    color: var(--card-white);
    font-size: 12px;
  }
  .contacts li {
    display: flex;
    justify-content: flex-end;
    align-items: center;
    gap: 7px;
    height: 18px;
  }
  .contacts__icon {
    width: 12px;
    height: 12px;
    flex: none;
  }
  .contacts__spacer { width: 12px; flex: none; }

  /* Back face */
  .card--back {
    background: var(--brand-blue);
    display: flex;
    align-items: center;
    justify-content: center;
  }
  .card--back .wordmark { position: static; flex-direction: column; gap: 14px; }
  .card--back .wordmark__mark { background: var(--card-white); width: 40px; height: 40px; }
  .card--back .wordmark__name {
    color: var(--card-white);
    font-size: 26px;
    text-align: center;
  }
</style>
</head>
<body>
<main class="sheet">

  <section class="card card--front" aria-label="Business card front">
    <svg class="card__waves" viewBox="0 0 520 318" width="520" height="318" aria-hidden="true">
      <path d="M0,112 C150,114 330,134 520,172 L520,180 C330,144 150,126 0,126 Z" fill="var(--wave-grey)"/>
      <path d="M0,144 C150,146 330,164 520,188 L520,318 L0,318 Z" fill="var(--brand-blue)"/>
      <path d="M0,155 C150,157 330,176 520,200" fill="none" stroke="var(--card-white)" stroke-width="1.5"/>
    </svg>

    <div class="wordmark">
      <span class="wordmark__mark"></span>
      <span class="wordmark__name">Steadfast<br>Property Reviews</span>
    </div>

    <div class="holder">
      <p class="holder__name">Mr Daniel Hart</p>
      <p class="holder__role">Managing Director</p>
    </div>

    <ul class="contacts">
      <li>PO Box 2246, Elmwood Park 3342<span class="contacts__spacer"></span></li>
      <li>03 5550 1842
        <svg class="contacts__icon" viewBox="0 0 12 12" aria-hidden="true">
          <circle cx="6" cy="6" r="6" fill="var(--card-white)"/>
          <path d="M3.6,3 L5,3 L5.5,4.6 L4.7,5.2 C5.1,6.1 5.9,6.9 6.8,7.3 L7.4,6.5 L9,7 L9,8.4 C6,8.6 3.4,6 3.6,3 Z" fill="var(--brand-blue)"/>
        </svg>
      </li>
      <li>0400 555 918
        <svg class="contacts__icon" viewBox="0 0 12 12" aria-hidden="true">
          <circle cx="6" cy="6" r="6" fill="var(--card-white)"/>
          <rect x="4.2" y="2.5" width="3.6" height="7" rx="0.6" fill="var(--brand-blue)"/>
          <rect x="4.8" y="3.3" width="2.4" height="4.4" fill="var(--card-white)"/>
        </svg>
      </li>
      <li>enquiries@steadfastpropertyreviews.com.au
        <svg class="contacts__icon" viewBox="0 0 12 12" aria-hidden="true">
          <circle cx="6" cy="6" r="6" fill="var(--card-white)"/>
          <rect x="3" y="4" width="6" height="4.2" fill="var(--brand-blue)"/>
          <path d="M3,4 L6,6.4 L9,4" fill="none" stroke="var(--card-white)" stroke-width="0.7"/>
        </svg>
      </li>
      <li>www.steadfastpropertyreviews.com.au
        <svg class="contacts__icon" viewBox="0 0 12 12" aria-hidden="true">
          <circle cx="6" cy="6" r="6" fill="var(--card-white)"/>
          <circle cx="6" cy="6" r="3.4" fill="none" stroke="var(--brand-blue)" stroke-width="0.8"/>
          <ellipse cx="6" cy="6" rx="1.4" ry="3.4" fill="none" stroke="var(--brand-blue)" stroke-width="0.7"/>
          <line x1="2.6" y1="6" x2="9.4" y2="6" stroke="var(--brand-blue)" stroke-width="0.7"/>
        </svg>
      </li>
    </ul>
  </section>

  <section class="card card--back" aria-label="Business card back">
    <div class="wordmark">
      <span class="wordmark__mark"></span>
      <span class="wordmark__name">Steadfast<br>Property Reviews</span>
    </div>
  </section>

</main>
</body>
</html>
```